Bright Pelvic Health Business Card

Need a business card for a surgical practice called Bright Pelvic Health. We have recently selected a logo (attached). The business card will need to have two formats:
1) One with the logo/physician name/ contact info on the front and location information on the back.
2) One in "appointment reminder card" style with the logo/ contact info/ date/ time on the front and the location information on the back.

The front side should include the following information:
- Logo
- Ravi K. Desai, MD FACOG
- phone: 469-555-0182
- fax: 1-469-555-0147
- email: admin@brightpelvic.example
- website: www.brightpelvichealth.example

The back side should have the office locations listed:
4812 Quarry Bend Dr, Plano, TX 75093
3650 Wrenfield Rd, Plano, TX 75025
2245 Brambleton Ln, Irving, TX 75038
915 S Garnet Ave B314, Dallas, TX 75201
1836 Tillman Pkwy, Grand Prairie, TX 75051
6417 Dorrance Way Dr, San Antonio, TX 78240
5920 Kessler Rd, Pasadena, TX 77504

Target Market(s)

1. Other physicians who might refer patients
2. Female patients

Industry/Entity Type

Business

Font styles to use
Other font styles liked:
• Tahoma for lettering

Requirements
Must have
• As per the instructions
Should not have
• No other images needed -- please try to keep font consistent with logo design. Can use Tahoma as the font for lettering.

```html
<!DOCTYPE html>
<html lang="en">
<head>
<meta charset="utf-8">
<title>Bright Pelvic Health – Business Card</title>
<link href="https://fonts.googleapis.com/css2?family=Open+Sans:wght@400;700&family=Questrial&display=swap" rel="stylesheet">
<style>
  :root{
    --page:#ffffff;
    --card:#f6f6f6;
    --card-edge:#e3e3e3;
    --ink:#2b2b2b;
    --soft-ink:#4a4a4a;
    --label:#9a9a9a;
    --brand-blue:#2f6db5;
    --accent-red:#e8323c;
  }
  *{box-sizing:border-box;margin:0;padding:0}
  html,body{width:1200px;height:582px;overflow:hidden;background:var(--page)}
  .stage{position:relative;width:1200px;height:582px;border:1px solid #d6d6d6}
  .side-label{position:absolute;top:66px;font:15px Arial,Helvetica,sans-serif;color:var(--label)}
  .card{position:absolute;top:102px;width:519px;height:339px;background:var(--card);border:1px solid var(--card-edge)}
  .card--front{left:81px}
  .card--back{left:600px;border-left:1px solid #dcdcdc}

  .physician{position:absolute;left:30px;top:27px;padding-left:9px;border-left:3px solid var(--brand-blue)}
  .physician__name{font:700 21px/1.1 "Open Sans",sans-serif;color:var(--ink)}
  .physician__title{font:400 14px/1.3 "Open Sans",sans-serif;color:var(--ink)}

  .brand{position:absolute;left:0;right:0;top:186px;display:flex;align-items:center;justify-content:center;gap:10px}
  .brand__dot{width:18px;height:18px;border-radius:50%;background:var(--accent-red)}
  .brand__name{font:700 28px/1 "Open Sans",sans-serif;color:var(--brand-blue)}

  .contact{position:absolute;font:14px/27px "Questrial",sans-serif;color:var(--soft-ink);list-style:none}
  .contact li{display:flex;align-items:center;gap:8px}
  .contact svg{width:13px;height:13px;flex:none}
  .contact--online{left:29px;top:266px}
  .contact--phone{left:266px;top:262px}

  .emblem-area{position:absolute;left:0;top:62px;width:132px;height:198px;border-radius:0 60% 60% 0;
    background:linear-gradient(120deg,rgba(47,109,181,.55),rgba(232,50,60,.35) 70%,rgba(246,246,246,0))}
  .locations{position:absolute;left:182px;top:24px}
  .locations__title{font:700 22px/1.2 "Open Sans",sans-serif;color:var(--brand-blue);margin-bottom:4px}
  .locations__list{list-style:none;font:15px/27.4px "Questrial",sans-serif;color:var(--soft-ink)}
</style>
</head>
<body>
<main class="stage">
  <span class="side-label" style="left:79px">Front</span>
  <span class="side-label" style="left:600px">Back</span>

  <section class="card card--front" aria-label="Card front">
    <div class="physician">
      <p class="physician__name">Ravi K. Desai,</p>
      <p class="physician__title">MD FACOG</p>
    </div>

    <div class="brand">
      <span class="brand__dot"></span>
      <span class="brand__name">Bright Pelvic Health</span>
    </div>

    <ul class="contact contact--online">
      <li><svg viewBox="0 0 14 14"><rect x="1" y="3" width="12" height="8" fill="none" stroke="#444" stroke-width="1.2"/><path d="M1 3l6 5 6-5" fill="none" stroke="#444" stroke-width="1.2"/></svg>admin@brightpelvic.example</li>
      <li><svg viewBox="0 0 14 14"><circle cx="7" cy="7" r="5.6" fill="none" stroke="#444" stroke-width="1.3"/><path d="M1.5 7h11M7 1.5c2.5 3 2.5 8 0 11M7 1.5c-2.5 3-2.5 8 0 11" fill="none" stroke="#444" stroke-width="1"/></svg>www.brightpelvichealth.example</li>
    </ul>

    <ul class="contact contact--phone">
      <li><svg viewBox="0 0 14 14"><rect x="4" y="1" width="6.5" height="12" rx="1.2" fill="none" stroke="#444" stroke-width="1.3"/><rect x="5.5" y="3" width="3.5" height="3" fill="#444"/></svg>469-555-0182</li>
      <li><svg viewBox="0 0 14 14"><rect x="4" y="1" width="6" height="4" fill="none" stroke="#444" stroke-width="1.2"/><rect x="1.5" y="5" width="11" height="5" fill="#444"/><rect x="4" y="10" width="6" height="3" fill="none" stroke="#444" stroke-width="1.2"/></svg>1-469-555-0147</li>
    </ul>
  </section>

  <section class="card card--back" aria-label="Card back">
    <div class="emblem-area" role="img" aria-label="Practice emblem artwork in blue and red"></div>
    <div class="locations">
      <h2 class="locations__title">lOCATIONS</h2>
      <ul class="locations__list">
        <li>4812 Quarry Bend Dr, Plano, TX 75093</li>
        <li>3650 Wrenfield Rd, Plano, TX 75025</li>
        <li>2245 Brambleton Ln, Irving, TX 75038</li>
        <li>915 S Garnet Ave B314, Dallas, TX 75201</li>
        <li>1836 Tillman Pkwy, Grand Prairie, TX 75051</li>
        <li>6417 Dorrance Way Dr, San Antonio, TX 78240</li>
        <li>5920 Kessler Rd, Pasadena, TX 77504</li>
      </ul>
    </div>
  </section>
</main>
</body>
</html>
```